Design concept for BrightKestrel.com Support Page

We are about to launch a new support page for our www.brightkestrel.com service for photographers and visual artists. The service provides media management, cloud storage, promotional and secure distribution to our members.

The support page will include FAQs and video tutorials.

In particular we're looking for a header for this page that suggests the user is in the support area of our service - so perhaps an illustration that suggests support could look nice (perhaps repair man or doctor iconography). Something to give this area of our site a different look and something that looks both cool and friendly.

Currently the page looks distinctly sparse and undesigned (see attached screenshot) - something that could be remedied, we feel, by some subtle design enhancements that we can implement using CSS.

```html
<!DOCTYPE html>
<html lang="en">
<head>
<meta charset="utf-8">
<title>BrightKestrel Support</title>
<link href="https://fonts.googleapis.com/css2?family=Open+Sans:wght@300;400;600;700&family=Arimo:wght@400;700&display=swap" rel="stylesheet">
<style>
  :root {
    --white: #ffffff;
    --ink: #4a4a4a;
    --muted: #7a7a7a;
    --hero: #77a3a7;
    --hero-accent: #f6d48b;
    --orange: #f26522;
    --slate: #5e6571;
    --faq-open: #8a8a8a;
    --faq-closed: #f4f4f4;
    --faq-border: #dcdcdc;
    --video-band: #808080;
    --arrow-box: #555555;
    --footer: #000000;
    --footer-link: #c9c9c9;
    --footer-dim: #8a8a8a;
  }
  * { box-sizing: border-box; margin: 0; padding: 0; }
  h1, h2, h3 { font-weight: 400; }
  html, body { width: 841px; height: 1200px; overflow: hidden; }
  body { position: relative; background: var(--white); font-family: "Open Sans", sans-serif; color: var(--ink); }

  .site-header { position: absolute; left: 0; top: 0; width: 841px; height: 70px; }
  .brand { position: absolute; left: 72px; top: 18px; display: flex; align-items: center; gap: 8px; }
  .brand-mark { width: 22px; height: 22px; background: var(--orange); border-radius: 4px; }
  .brand-name { font-size: 22px; font-weight: 700; color: #555; letter-spacing: -0.3px; }
  .user { position: absolute; left: 682px; top: 18px; display: flex; align-items: center; gap: 8px; }
  .user-avatar { width: 28px; height: 28px; border-radius: 50%; background: linear-gradient(135deg, #8b7a6a, #3b3430); }
  .user-name { font-size: 10px; color: #444; }

  .hero { position: absolute; left: 0; top: 70px; width: 841px; height: 178px; background: var(--hero); }
  .hero-title { position: absolute; left: 72px; top: 40px; font-size: 37px; font-weight: 300; color: var(--white); letter-spacing: -0.3px; }
  .hero-subtitle { position: absolute; left: 72px; top: 88px; font-size: 26px; font-weight: 600; color: var(--hero-accent); }
  .hero-illustration { position: absolute; left: 568px; top: 8px; width: 190px; height: 162px; border-radius: 4px;
    background: radial-gradient(circle at 50% 45%, #f3c39a 0%, #5a6a70 55%, rgba(119,163,167,0) 80%); }

  .intro { position: absolute; left: 110px; top: 274px; width: 621px; text-align: center; font-size: 12px; line-height: 19px; color: var(--muted); }

  .kb-search { position: absolute; left: 70px; top: 347px; width: 701px; height: 67px; background: var(--slate); }
  .kb-title { position: absolute; left: 28px; top: 18px; font-family: "Arimo", sans-serif; font-size: 24px; font-weight: 400; color: var(--white); white-space: nowrap; }
  .kb-field { position: absolute; left: 343px; top: 17px; width: 330px; height: 33px; background: var(--white); border-radius: 2px; }
  .kb-placeholder { position: absolute; left: 11px; top: 8px; font-size: 11px; color: #999; }
  .kb-button { position: absolute; right: 7px; top: 7px; width: 48px; height: 19px; background: var(--orange); color: var(--white);
    font-size: 8.5px; font-weight: 600; text-align: center; line-height: 19px; border-radius: 2px; }

  .faq-heading { position: absolute; left: 71px; top: 449px; font-family: "Arimo", sans-serif; font-size: 24px; font-weight: 400; color: var(--orange); }
  .faq-item { position: absolute; left: 71px; width: 700px; }
  .faq-item.is-closed { height: 51px; background: var(--faq-closed); border: 1px solid var(--faq-border); }
  .faq-item.is-open { top: 498px; height: 124px; background: var(--faq-open); }
  .faq-icon { position: absolute; left: 20px; width: 22px; height: 22px; border-radius: 50%; text-align: center; line-height: 22px;
    font-family: "Arimo", sans-serif; font-weight: 700; font-size: 12px; }
  .is-closed .faq-icon { top: 14px; background: var(--orange); color: var(--white); }
  .is-open .faq-icon { top: 16px; background: var(--white); color: var(--orange); }
  .faq-question { position: absolute; left: 50px; font-family: "Arimo", sans-serif; font-size: 13px; font-weight: 400; white-space: nowrap; }
  .is-closed .faq-question { top: 16px; color: var(--orange); }
  .is-open .faq-question { top: 20px; color: var(--white); }
  .faq_answer_unused { display: none; }
  .faq-answer { position: absolute; left: 52px; top: 45px; width: 628px; font-family: "Arimo", sans-serif; font-weight: 700; font-size: 7.7px; line-height: 18.4px; color: var(--white); }

  .videos { position: absolute; left: 0; top: 856px; width: 841px; height: 238px; background: var(--video-band); }
  .videos-title { position: absolute; left: 0; top: 22px; width: 841px; text-align: center; font-size: 29px; font-weight: 400; color: var(--white); }
  .carousel-arrow { position: absolute; top: 94px; width: 40px; height: 50px; background: var(--arrow-box); }
  .carousel-arrow.prev { left: 0; }
  .carousel-arrow.next { left: 801px; }
  .carousel-arrow svg { display: block; }
  .video-card { position: absolute; top: 80px; width: 161px; text-align: center; }
  .video-thumb { position: relative; width: 161px; height: 99px; }
  .video-thumb svg { position: absolute; left: 62px; top: 31px; }
  .video-caption { margin-top: 12px; font-size: 10.4px; line-height: 14.5px; color: var(--white); }

  .site-footer { position: absolute; left: 0; top: 1094px; width: 841px; height: 106px; background: var(--footer); text-align: center; }
  .footer-links { position: absolute; top: 21px; width: 841px; font-size: 9.6px; color: var(--footer-link); }
  .footer-links .sep { margin: 0 6px; }
  .copyright { position: absolute; top: 53px; width: 841px; font-size: 9.2px; color: var(--white); }
  .powered { position: absolute; top: 66px; width: 841px; font-size: 9.2px; color: var(--footer-dim); }
</style>
</head>
<body>

<header class="site-header">
  <div class="brand"><span class="brand-mark"></span><span class="brand-name">BrightKestrel</span></div>
  <div class="user">
    <div class="user-avatar" role="img" aria-label="User profile photo"></div>
    <span class="user-name">Mara Lindqvist</span>
  </div>
</header>

<section class="hero">
  <h1 class="hero-title">We’re Happy To Help...</h1>
  <h2 class="hero-subtitle">BrightKestrel Support</h2>
  <div class="hero-illustration" role="img" aria-label="Cartoon of a repairman with a wrench and a cheerful user jumping from an office chair"></div>
</section>

<p class="intro">Aliquam erat volutpat. Etiam luctus rutrum diam sit amet egestas. Mauris et odio nisl. Cras vulputate mi quis neque venenatis, vitae lacinia magna euismod. Aliquam tincidunt velit et diam mattis iaculis.</p>

<section class="kb-search">
  <h2 class="kb-title">Search our Knowledge Base</h2>
  <div class="kb-field">
    <span class="kb-placeholder">Search</span>
    <span class="kb-button">SEARCH</span>
  </div>
</section>

<h2 class="faq-heading">Faq’s</h2>

<div class="faq-item is-open">
  <span class="faq-icon">?</span>
  <h3 class="faq-question">Uploading files using the Drag and Drop Uploader</h3>
  <p class="faq-answer">It is a long established fact that a reader will be distracted by the readable content of a page when looking at its layout. The point of using Lorem Ipsum is that it has a more-or-less normal distribution of letters, as opposed to using 'Content here, content here', making it look like readable English. Many desktop publishing packages and web page editors now use Lorem Ipsum as their default model text, and a search for 'lorem ipsum' will uncover many web sites still in their infancy.</p>
</div>
<div class="faq-item is-closed" style="top:629px"><span class="faq-icon">?</span><h3 class="faq-question">Uploading files using the Drag and Drop Uploader</h3></div>
<div class="faq-item is-closed" style="top:688px"><span class="faq-icon">?</span><h3 class="faq-question">Uploading files using the Drag and Drop Uploader</h3></div>
<div class="faq-item is-closed" style="top:746px"><span class="faq-icon">?</span><h3 class="faq-question">Uploading files using the Drag and Drop Uploader</h3></div>

<section class="videos">
  <h2 class="videos-title">Video Tutorials</h2>

  <div class="carousel-arrow prev"><svg width="40" height="50"><polyline points="24,10 12,25 24,40" fill="none" stroke="#ffffff" stroke-width="1.5"/></svg></div>
  <div class="carousel-arrow next"><svg width="40" height="50"><polyline points="16,10 28,25 16,40" fill="none" stroke="#ffffff" stroke-width="1.5"/></svg></div>

  <div class="video-card" style="left:71px">
    <div class="video-thumb" role="img" aria-label="Illustration of a hand cursor clicking an upload button" style="background:linear-gradient(180deg,#3b8ec9 0%,#cfd6db 45%,#e8ebee 100%)">
      <svg width="37" height="37"><circle cx="18.5" cy="18.5" r="16" fill="rgba(0,0,0,0.15)" stroke="#fff" stroke-width="2.5"/><polygon points="14,10 27,18.5 14,27" fill="#fff"/></svg>
    </div>
    <p class="video-caption">Uploading Files Using the<br>Drang and Drop Uploader</p>
  </div>
  <div class="video-card" style="left:250px">
    <div class="video-thumb" role="img" aria-label="Illustration of people arranging content on a large tablet" style="background:linear-gradient(160deg,#dfe6ea 0%,#b7a9b8 50%,#6f7f8c 100%)">
      <svg width="37" height="37"><circle cx="18.5" cy="18.5" r="16" fill="rgba(0,0,0,0.15)" stroke="#fff" stroke-width="2.5"/><polygon points="14,10 27,18.5 14,27" fill="#fff"/></svg>
    </div>
    <p class="video-caption">Publising Files</p>
  </div>
  <div class="video-card" style="left:430px">
    <div class="video-thumb" role="img" aria-label="Illustration of a designer at a desk surrounded by gallery pages" style="background:linear-gradient(180deg,#9fb9b8 0%,#8aa6a6 60%,#6f8a8e 100%)">
      <svg width="37" height="37"><circle cx="18.5" cy="18.5" r="16" fill="rgba(0,0,0,0.15)" stroke="#fff" stroke-width="2.5"/><polygon points="14,10 27,18.5 14,27" fill="#fff"/></svg>
    </div>
    <p class="video-caption">Creating Galleries</p>
  </div>
  <div class="video-card" style="left:610px">
    <div class="video-thumb" role="img" aria-label="Flat icon collage of portfolio and marketing tools" style="background:linear-gradient(135deg,#3f7fb8 0%,#e9b64a 50%,#d9573b 100%)">
      <svg width="37" height="37"><circle cx="18.5" cy="18.5" r="16" fill="rgba(0,0,0,0.15)" stroke="#fff" stroke-width="2.5"/><polygon points="14,10 27,18.5 14,27" fill="#fff"/></svg>
    </div>
    <p class="video-caption">Creating Portfolios</p>
  </div>
</section>

<footer class="site-footer">
  <nav class="footer-links">Home<span class="sep">·</span>Contact Us<span class="sep">·</span>Affiliate Program<span class="sep">·</span>Privacy Policy<span class="sep">·</span>Site Terms and Conditions<span class="sep">·</span>About Us</nav>
  <p class="copyright">© Copyright 2014 Northbay Images Pte Ltd. All rights reserved.</p>
  <p class="powered">Powered by BrightKestrel</p>
</footer>

</body>
</html>
```